Menu Board 1000mmx500mm re-design

I would like to re-design exiting menu board 1000mmx500mm. Current board letters are bit to small to read. I would like to have pictures (attached) of the food offered on it and at the same time to create balance between pictures and size of the text to be easily readable. Fonts and colours are up to designer choice but prefer warm and bright colours rather anything dark.

Target Market(s)

Food industry

Industry/Entity Type

Food

Font styles to use
Other font styles liked:
• I leave font choice to designer

Colors
FFC000
F8CF3A
FAE287
FDF2CF
FEFAEE
F0912C
F2A743
F7CA91
FBE8D2
FDF5EE
EE7325
F08F49
F5BC92
FAE3D3
FDF4ED

Requirements
Must have
• Pictures + Text
Nice to have
• Balance between images and text.
Should not have
• Can't think of any

```html
<!DOCTYPE html>
<html lang="en">
<head>
<meta charset="utf-8">
<title>Roti Chicken Menu Board</title>
<link rel="stylesheet" href="https://fonts.googleapis.com/css2?family=Asap+Condensed:wght@500;600&family=Itim&display=swap">
<style>
  :root {
    --cream: #FDF9EE;
    --orange: #EE7325;
    --orange-light: #F08F49;
    --ink: #2A2623;
    --photo-warm: #C9A27A;
    --photo-dark: #6E5A48;
  }
  html, body { margin: 0; padding: 0; overflow: hidden; }
  .board {
    position: relative;
    width: 1200px;
    height: 2400px;
    background: var(--cream);
    overflow: hidden;
    font-family: "Itim", sans-serif;
    color: var(--ink);
  }
  .art { position: absolute; left: 0; top: 0; }
  .item { position: absolute; left: 58px; width: 720px; }
  .item-head {
    display: flex;
    align-items: baseline;
    font-family: "Asap Condensed", sans-serif;
    font-weight: 500;
    font-size: 60px;
    line-height: 1;
    color: var(--orange);
    white-space: nowrap;
  }
  .item-leader { flex: 1; overflow: hidden; letter-spacing: 2px; }
  .item-leader::before { content: "......................................................................"; }
  .item-desc { font-size: 37px; line-height: 47px; margin-top: 6px; }
  .sauces { position: absolute; left: 62px; top: 2150px; width: 1100px; }
  .sauces-title {
    font-family: "Asap Condensed", sans-serif;
    font-weight: 500;
    font-size: 54px;
    color: var(--orange);
    line-height: 1;
  }
  .sauce-list {
    display: grid;
    grid-template-columns: 453px 294px auto;
    font-family: "Asap Condensed", sans-serif;
    font-weight: 600;
    font-size: 60px;
    line-height: 70px;
    margin-top: 12px;
  }
</style>
</head>
<body>
<main class="board">
  <svg class="art" width="1200" height="2400" viewBox="0 0 1200 2400">
    <defs>
      <linearGradient id="heroTone" x1="0" y1="0" x2="1" y2="1">
        <stop offset="0" stop-color="#6E5A48"/>
        <stop offset="0.5" stop-color="#C9A27A"/>
        <stop offset="1" stop-color="#8C7058"/>
      </linearGradient>
      <linearGradient id="wrapTone" x1="0" y1="0" x2="1" y2="1"><stop offset="0" stop-color="#8E3A4A"/><stop offset="1" stop-color="#D9C3A8"/></linearGradient>
      <linearGradient id="boxTone" x1="0" y1="0" x2="1" y2="1"><stop offset="0" stop-color="#B07A45"/><stop offset="1" stop-color="#EDE6D6"/></linearGradient>
      <linearGradient id="potatoTone" x1="0" y1="0" x2="1" y2="1"><stop offset="0" stop-color="#E9A93A"/><stop offset="1" stop-color="#C9781F"/></linearGradient>
      <linearGradient id="ciabattaTone" x1="0" y1="0" x2="0" y2="1"><stop offset="0" stop-color="#F3F1EE"/><stop offset="0.6" stop-color="#D8B17A"/><stop offset="1" stop-color="#B27A4A"/></linearGradient>
    </defs>
    <polygon points="0,0 1200,0 1200,915 0,640" fill="url(#heroTone)" role="img" aria-label="Photo of a grilled chicken wrap with kale, tomato, courgette and red onion"/>
    <line x1="0" y1="640" x2="1200" y2="915" stroke="var(--orange)" stroke-width="10"/>

    <circle cx="1014" cy="870" r="160" fill="var(--orange)"/>
    <circle cx="1000" cy="862" r="158" fill="url(#wrapTone)" role="img" aria-label="Photo of a beetroot wrap filled with salmon and salad"/>

    <circle cx="1014" cy="1210" r="160" fill="var(--orange)"/>
    <circle cx="1000" cy="1202" r="158" fill="url(#boxTone)" role="img" aria-label="Photo of roast chicken leg with veggie rice"/>

    <circle cx="1014" cy="1541" r="160" fill="var(--orange)"/>
    <circle cx="1000" cy="1533" r="158" fill="url(#potatoTone)" role="img" aria-label="Photo of roasted potatoes with thyme"/>

    <circle cx="1014" cy="1881" r="160" fill="var(--orange)"/>
    <circle cx="1000" cy="1873" r="158" fill="url(#ciabattaTone)" role="img" aria-label="Photo of a chicken ciabatta with rocket"/>
  </svg>

  <section class="item" style="top:842px">
    <div class="item-head"><span>CIABATTA</span><span class="item-leader"></span><span>£6</span></div>
    <p class="item-desc" style="margin:6px 0 0">Roti Chicken, Rucola, Caramelized Onions,<br>Tomato, Fresh onion</p>
  </section>
  <section class="item" style="top:1052px">
    <div class="item-head"><span>WRAP</span><span class="item-leader"></span><span>£7</span></div>
    <p class="item-desc" style="margin:6px 0 0">Roti Chicken, Crunchy Slaw,Tomato,<br>Fresh onion &amp; Sauce of your choice</p>
  </section>
  <section class="item" style="top:1261px">
    <div class="item-head"><span>BEETROOT WRAP</span><span class="item-leader"></span><span>£8</span></div>
    <p class="item-desc" style="margin:6px 0 0">Roti Chicken, Crunchy Slaw,Tomato,<br>Fresh onion &amp; Sauce of your choice</p>
  </section>
  <section class="item" style="top:1471px">
    <div class="item-head"><span>1/4 CHICKEN BOX</span><span class="item-leader"></span><span>£9</span></div>
    <p class="item-desc" style="margin:6px 0 0">Roti Chicken, Veggie Rice &amp; Salad</p>
  </section>
  <section class="item" style="top:1634px">
    <div class="item-head"><span>1/2 CHICKEN BOX</span><span class="item-leader"></span><span>£14</span></div>
    <p class="item-desc" style="margin:6px 0 0">Roti Chicken, Veggie Rice &amp; Salad</p>
  </section>
  <section class="item" style="top:1797px">
    <div class="item-head"><span>ROASTED POTATOES</span><span class="item-leader"></span><span>&nbsp;£2.5</span></div>
    <p class="item-desc" style="margin:6px 0 0">Thyme &amp; Garlic</p>
  </section>
  <section class="item" style="top:1960px">
    <div class="item-head"><span>WATER</span><span class="item-leader"></span><span>£1</span></div>
  </section>
  <section class="item" style="top:2030px">
    <div class="item-head"><span>CAN &amp; JUICES</span><span class="item-leader"></span><span>£1.8</span></div>
  </section>

  <section class="sauces">
    <h2 class="sauces-title" style="margin:0">SAUCES</h2>
    <div class="sauce-list">
      <span>Signature</span><span>BBQ</span><span>Garlic Mayo</span>
      <span>Sweet Chilli</span><span>Piri Piri</span><span></span>
    </div>
  </section>
</main>
</body>
</html>
```